Business Card design

Keen on a very modern design with using the red star as a feature point preferably will have it printed with red foiling.

Target Market(s)

Cosmetics

Industry/Entity Type

Cosmetics

Contact Information for Business Card

Marcie Budd
Director
9 Frey Avenue
Doveton West Victoria
Australia 3618
marcie@glowpactsupply.com.au

Font styles to use
Sans Serif

Colors
ec1f27
000000

Requirements
Must have
• Keen on some red stars on back with black background and I may get the red components printed as red foiling potentially

```html
<!DOCTYPE html>
<html lang="en">
<head>
<meta charset="utf-8">
<title>Glowpact Business Card</title>
<link rel="stylesheet" href="https://fonts.googleapis.com/css2?family=Roboto:wght@400;500;700;900&display=swap">
<style>
  :root {
    --brand-red: #ec1f27;
    --name-red: #c9212a;
    --black: #000000;
    --panel-dark: #0b0b0b;
    --panel-mid: #2a2a2a;
    --title-grey: #b9b0a4;
    --text-light: #d6d2cc;
    --card-light: #f2f0ed;
    --logo-ink: #1a1a1a;
    --page-bg: #e4e1dc;
  }
  * { margin: 0; padding: 0; box-sizing: border-box; }
  html, body {
    width: 1200px; height: 1047px; overflow: hidden;
    background: var(--page-bg);
    font-family: "Roboto", Arial, sans-serif;
  }
  .business-card {
    position: absolute; left: 80px; top: 243px;
    width: 1040px; height: 562px;
    background: var(--card-light);
    overflow: hidden;
    box-shadow: 0 2px 10px rgba(0,0,0,0.12);
  }
  .card-shapes { position: absolute; inset: 0; }
  .holder-name {
    position: absolute; left: 53px; top: 104px;
    font-size: 50px; font-weight: 500; letter-spacing: 1.5px;
    color: var(--name-red); line-height: 1;
  }
  .holder-title {
    position: absolute; left: 54px; top: 165px;
    font-size: 29px; font-weight: 500; letter-spacing: 1px;
    color: var(--title-grey); line-height: 1;
  }
  .address {
    position: absolute; left: 54px; top: 342px;
    font-size: 20px; line-height: 31px; letter-spacing: 0.8px;
    color: var(--text-light);
  }
  .contact-list {
    position: absolute; left: 54px; top: 431px;
    list-style: none;
  }
  .contact-list li {
    display: flex; align-items: center;
    height: 31px;
    font-size: 21px; letter-spacing: 0.5px;
    color: var(--text-light);
  }
  .contact-icon { width: 20px; height: 20px; margin-right: 20px; flex: none; }
  .contact-list .accent { color: var(--name-red); }
  .company-mark {
    position: absolute; left: 578px; top: 252px;
    display: flex; align-items: center; gap: 12px;
  }
  .company-dot {
    width: 34px; height: 34px; border-radius: 50%;
    background: var(--brand-red);
  }
  .company-name {
    font-size: 66px; font-weight: 900; letter-spacing: -1px;
    color: var(--logo-ink); line-height: 1;
  }
</style>
</head>
<body>
  <div class="business-card">
    <svg class="card-shapes" width="1040" height="562" viewBox="0 0 1040 562" aria-hidden="true">
      <defs>
        <linearGradient id="panelShade" x1="0" y1="0" x2="1" y2="0.3">
          <stop offset="0" stop-color="#1c1c1c"/>
          <stop offset="0.55" stop-color="#0c0c0c"/>
          <stop offset="1" stop-color="#000"/>
        </linearGradient>
        <linearGradient id="swooshRed" x1="0" y1="0" x2="0" y2="1">
          <stop offset="0" stop-color="#ec1f27"/>
          <stop offset="0.6" stop-color="#c3161d"/>
          <stop offset="1" stop-color="#7c0d11"/>
        </linearGradient>
      </defs>
      <path class="dark-panel" d="M0 0 H668 C560 90 470 300 627 562 H0 Z" fill="url(#panelShade)"/>
      <path class="red-swoosh" d="M668 0 C545 95 430 320 598 562 L580 562 C440 330 525 110 632 0 Z" fill="url(#swooshRed)"/>
    </svg>

    <div class="holder-name">Marcie Budd</div>
    <div class="holder-title">Director</div>

    <div class="address">9 Frey Avenue,Doveton West Victoria,<br>Australia 3618</div>

    <ul class="contact-list">
      <li>
        <svg class="contact-icon" viewBox="0 0 20 20" aria-hidden="true">
          <path d="M5 2 L8 6 L6 8 C7 11 9 13 12 14 L14 12 L18 15 L16 18 C9 18 2 11 2 4 Z" fill="none" stroke="#c9212a" stroke-width="1.6"/>
        </svg>
        000 482 7719
      </li>
      <li>
        <svg class="contact-icon" viewBox="0 0 20 20" aria-hidden="true">
          <rect x="2" y="5" width="16" height="11" fill="#c9212a"/>
          <path d="M2 5 L10 11 L18 5" fill="none" stroke="#0b0b0b" stroke-width="1.4"/>
        </svg>
        marcie@glowpactsupply.com.au
      </li>
      <li>
        <svg class="contact-icon" viewBox="0 0 20 20" aria-hidden="true">
          <g fill="none" stroke="#c9212a" stroke-width="1.4">
            <circle cx="10" cy="10" r="8"/>
            <ellipse cx="10" cy="10" rx="3.5" ry="8"/>
            <line x1="2" y1="10" x2="18" y2="10"/>
          </g>
        </svg>
        <span>www.<span class="accent">glowpactsupply</span>.com.au</span>
      </li>
    </ul>

    <div class="company-mark">
      <span class="company-dot"></span>
      <span class="company-name">Glowpact</span>
    </div>
  </div>
</body>
</html>
```